Labels for essential oils small botlles

We are Slovenia based company Velmira botanic Ltd. www.velmira-botanic.example We offer essential oils as pure essential oils or blends (mixed) essential oils. We have different kind of essential oils 40+ and blends. We sell in different sizes as: 10ml, 30ml, 50ml and 100ml. But majority is 10ml.
All essential oils are in glass bottles with closer. We will now change bottles style from amber to cobalt blue with black closure (see picture attached)
We would like to have different stile of label for different category of essential oils. Here is link about different categories of essential oils https://www.quillfernguide.example/blending-essential-oils/ . The different style / color could be by note:
- Top notes
- Middle notes
- Base notes
- Mixes – different oils mixed together and named as chill out, deep breath, sleep well, etc
Possible is also differentiation regarding:
• Citrus
• Floral
• Herbaceous
• Camphoraceous
• Spicy
• Resinous
• Woody
• Earthy
• Mixes

On labels should be also pictograms according to REACH directive of EU and label according to CPL (see attached file). We would also like to add EAN code attached on the edge of the label. On label is some text fixed I try to show in pdf attached file and some is variable depends from essential oil and date of production.

Meaning we need general labels for each note or other classification and one for mixes – you could also show your option or classification on something else with story behind.

10 ml roll 30 mm x 70 mm (1,25”x3”) but finial dimensions will follow.

We use Tavorin Kp520 printer. For editing labels we use TagWeaver which support also EAN codes. We import labels as picture in background or different according to your instructions.

Target Market(s)

Retail, health and wellness, all audiences and web shop

Industry/Entity Type

Health And Wellness

Font styles to use
Other font styles liked:
• PostMedRg is our font but could be different

Colors

Designer to choose colors to be used in the design.

Requirements
Must have
• Label should be as template that we could use for different oils in same group. More in attached document. According to CLP we have to put red pictograms on labels which is not nice and should be some how nicely integrated. on the edge EAB dar code that products could be sell through online.
Nice to have
• Different colours, some symbol as a drop or flower or herb. Logo is not necessary that is on label. We would like that label it self represent our brand.

```html
<!DOCTYPE html>
<html lang="en">
<head>
<meta charset="utf-8">
<title>Velmira Botanic – Essential Oil Labels</title>
<link rel="stylesheet" href="https://fonts.googleapis.com/css2?family=Oswald:wght@400;500;600&family=Roboto:wght@400;500;700&display=swap">
<style>
  :root {
    --canvas: #f4f4f3;
    --pine-light: #d08fb9;
    --pine-dark: #a35a88;
    --melisa-light: #a6cb2a;
    --melisa-dark: #4f8a10;
    --text-light: #ffffff;
    --band: #efefeb;
    --band-text: #1d1d1d;
    --dots: rgba(255, 255, 255, 0.9);
    --brand-text: rgba(255, 255, 255, 0.88);
  }
  * { box-sizing: border-box; margin: 0; padding: 0; }
  html, body {
    width: 1200px;
    height: 1090px;
    overflow: hidden;
    background: var(--canvas);
  }
  .label-sheet {
    position: relative;
    width: 1200px;
    height: 1090px;
  }
  .label {
    position: absolute;
    top: 480px;
    width: 312px;
    height: 435px;
    color: var(--text-light);
    font-family: "Oswald", sans-serif;
    overflow: hidden;
  }
  .label--pine {
    left: 146px;
    background: linear-gradient(90deg, var(--pine-light), var(--pine-dark));
  }
  .label--melisa {
    left: 656px;
    background: linear-gradient(90deg, var(--melisa-light), var(--melisa-dark));
  }
  .label__ornament {
    position: absolute;
    top: 30px;
    right: 0;
    width: 66px;
    height: 240px;
    border-radius: 120px 0 0 120px;
  }
  .label--pine .label__ornament {
    background: radial-gradient(circle at 90% 50%, rgba(255,255,255,0.32), rgba(255,255,255,0.06) 75%);
  }
  .label--melisa .label__ornament {
    background: radial-gradient(circle at 90% 50%, rgba(30,80,10,0.5), rgba(30,80,10,0.08) 75%);
  }
  .label__local-name {
    position: absolute;
    left: 50px;
    top: 34px;
    font-size: 29px;
    font-weight: 500;
    line-height: 1.1;
  }
  .label__title {
    position: absolute;
    left: 50px;
    top: 88px;
    font-size: 50px;
    font-weight: 600;
    line-height: 48px;
  }
  .label__divider {
    position: absolute;
    left: 50px;
    top: 238px;
    width: 142px;
    border-top: 2px dotted var(--dots);
  }
  .label__latin {
    position: absolute;
    left: 50px;
    top: 250px;
    font-size: 20px;
    font-weight: 500;
    line-height: 30px;
  }
  .label__band {
    position: absolute;
    left: 0;
    top: 315px;
    width: 100%;
    height: 54px;
    background: var(--band);
    color: var(--band-text);
    font-family: "Roboto", sans-serif;
    font-size: 23px;
    font-weight: 500;
    line-height: 54px;
    padding-left: 50px;
  }
  .label__band strong { font-weight: 700; }
  .label__brand {
    position: absolute;
    left: 0;
    top: 382px;
    width: 100%;
    text-align: center;
    font-family: "Roboto", sans-serif;
    font-size: 16px;
    font-weight: 400;
    letter-spacing: 2px;
    color: var(--brand-text);
  }
</style>
</head>
<body>
<main class="label-sheet">

  <section class="label label--pine">
    <div class="label__ornament" role="img" aria-label="Decorative leafy branch pattern"></div>
    <p class="label__local-name">SREBRNA JELKA</p>
    <h2 class="label__title">PINE<br>ESSENTIAL<br>OIL</h2>
    <div class="label__divider"></div>
    <p class="label__latin">PINUS NIGRA<br>TWIG LEAFOI</p>
    <p class="label__band"><strong>100%</strong> Organic</p>
    <p class="label__brand">VELMIRA BOTANIC</p>
  </section>

  <section class="label label--melisa">
    <div class="label__ornament" role="img" aria-label="Decorative leafy branch pattern"></div>
    <p class="label__local-name">MELISA</p>
    <h2 class="label__title">MELISA<br>ESSENTIAL<br>OIL</h2>
    <div class="label__divider"></div>
    <p class="label__latin">CYMBOPOGON<br>WINTERIANUS</p>
    <p class="label__band"><strong>100%</strong> Organic</p>
    <p class="label__brand">VELMIRA BOTANIC</p>
  </section>

</main>
</body>
</html>
```